Ridge Gathering presented by The Keystone

This is a one-day seminar for men who want to grow mentally, spiritually and financially.
Host Pastor Darnell Whitford
Special guest: Dr. Vernon Blake, Dr. Simone Harker

Target Market(s)

Men 18-55

Colors

Designer to choose colors to be used in the design.

Requirements
Must have
• clean designs
Nice to have
• A clean design that translates to social media and websites

```html
<!DOCTYPE html>
<html lang="en">
<head>
<meta charset="utf-8">
<title>Ridge Gathering – The Keystone</title>
<link rel="stylesheet" href="https://fonts.googleapis.com/css2?family=Roboto+Condensed:wght@300;400;700;800&display=swap">
<style>
  :root {
    --canvas: #ececec;
    --paper-top: #ebe7e7;
    --paper-bottom: #d3cbcc;
    --ink: #1c1c1c;
    --red: #c01f2f;
    --white: #ffffff;
    --rule: #6d6d6d;
  }
  * { margin: 0; padding: 0; box-sizing: border-box; }
  html, body { width: 1200px; height: 1200px; overflow: hidden; background: var(--canvas); }
  body { font-family: "Roboto Condensed", Arial, sans-serif; color: var(--ink); }

  .flyer {
    position: absolute; left: 152px; top: 20px;
    width: 896px; height: 1160px; overflow: hidden;
    background: linear-gradient(180deg, var(--paper-top) 0%, var(--paper-bottom) 70%);
    box-shadow: 0 12px 30px rgba(0,0,0,0.25);
  }
  .flyer-shapes { position: absolute; inset: 0; }

  .header-band { position: absolute; left: 0; top: 84px; width: 896px; height: 123px; background: var(--white); }
  .bar { position: absolute; height: 22px; }
  .bar.black { background: var(--ink); top: 62px; }
  .bar.red { background: var(--red); top: 207px; }
  .bar.left { left: 0; width: 66px; }
  .bar.right { left: 397px; width: 499px; }

  .brand {
    position: absolute; left: 66px; top: 62px; width: 331px; height: 168px;
    display: flex; align-items: center; justify-content: center; gap: 12px;
  }
  .brand-dot { width: 22px; height: 22px; border-radius: 50%; background: var(--red); }
  .brand-name { font-weight: 700; font-size: 46px; color: var(--ink); letter-spacing: 0.5px; }

  .event-title { position: absolute; left: 420px; width: 440px; text-align: center; }
  .event-title .seminar { position: absolute; top: 100px; width: 100%; font-weight: 700; font-size: 46px; line-height: 1; }
  .event-title .audience { position: absolute; top: 162px; width: 100%; font-weight: 700; font-size: 31px; line-height: 1; color: var(--red); letter-spacing: 11px; }

  .headline { position: absolute; left: 40px; width: 856px; text-align: center; line-height: 1; }
  .headline .light { font-weight: 300; font-size: 60px; display: block; position: absolute; width: 100%; }
  .headline .grow { font-weight: 800; font-style: italic; color: var(--red); }
  .headline .strong { font-weight: 700; font-size: 50px; display: block; position: absolute; width: 100%; }

  .speakers-photo {
    position: absolute; left: 92px; top: 556px; width: 704px; height: 431px;
    background: radial-gradient(ellipse at 50% 40%, #b9b0b1 0%, #9d9495 45%, rgba(60,55,56,0.85) 100%);
    border-radius: 6px 6px 0 0;
  }

  .credits { position: absolute; left: 0; width: 896px; text-align: center; color: var(--white); font-size: 33px; line-height: 1; }
  .credits b { font-weight: 700; }
  .credits span { font-weight: 300; }

  .contact {
    position: absolute; left: 0; top: 1104px; width: 896px;
    display: flex; align-items: center; justify-content: center; gap: 20px;
    color: var(--white); font-weight: 700; font-size: 19px;
  }
  .contact .rule { flex: 1; height: 3px; border-top: 1px solid var(--rule); border-bottom: 1px solid var(--rule); opacity: 0.8; }
</style>
</head>
<body>
  <main class="flyer">
    <svg class="flyer-shapes" width="896" height="1160" viewBox="0 0 896 1160" aria-hidden="true">
      <path d="M0 706 Q430 1246 896 676 L896 1160 L0 1160 Z" fill="var(--red)"/>
      <path d="M0 722 Q430 1262 896 694 L896 1160 L0 1160 Z" fill="var(--ink)"/>
    </svg>

    <div class="header-band"></div>
    <div class="bar black left"></div>
    <div class="bar black right"></div>
    <div class="bar red left"></div>
    <div class="bar red right"></div>

    <div class="brand">
      <span class="brand-dot"></span>
      <span class="brand-name">The Keystone</span>
    </div>

    <div class="event-title">
      <div class="seminar">ONE-DAY SEMINAR</div>
      <div class="audience">FOR MEN</div>
    </div>

    <h1 class="headline">
      <span class="light" style="top:286px">WHO WANT</span>
      <span class="light" style="top:346px">TO <span class="grow">GROW</span></span>
      <span class="strong" style="top:418px">MENTALLY, SPIRITUALLY</span>
      <span class="strong" style="top:479px">AND FINANCIALLY.</span>
    </h1>

    <div class="speakers-photo" role="img" aria-label="Photo of the host and two special guests standing together"></div>

    <div class="credits" style="top:1008px"><b>HOST</b> <span>PASTOR DARNELL WHITFORD</span></div>
    <div class="credits" style="top:1050px"><b>SPECIAL GUEST:</b> <span>DR. VERNON BLAKE, DR. SIMONE HARKER</span></div>

    <div class="contact">
      <span class="rule"></span>
      <span>FOR MORE INFO CALL US 555 0142 780</span>
      <span class="rule"></span>
    </div>
  </main>
</body>
</html>
```